Website front end design for an education nonprofit

This project involves design and development of the website front end (i.e., Web user interface and user experience design) for PAVO Tides, a nonprofit initiative for developing an online platform for basic English language instruction, especially targeted toward underprivileged, non-native English speaking populations.

More about us: We are a team of educators, researchers and engineers passionate about this cause and would like to invite talented, creative web developers to join us in this effort to create positive social impact! Please send a personal message to the project owner for the executive summary to get more information about our initiative, big picture vision and the team.

PAVO Tides website front end (UI/UX) design
Our key goals for this project are to develop an impressive Drupal-based front end for our website as well as to find really talented and creative web/UI/UX designers-cum-developers who are experts in the state-of-the-art web technologies, and are passionate about the cause of global online basic education. At the end of this project, we hope to have long term engagement with the selected developer(s) for our future website design and development needs.

Here are some preliminary guidelines on the PAVO Tides website front end framework as envisioned by us so far. Please note that we would very much encourage creative ideas and mock-ups from the developers.

1. Current platform: Our website prototype back-end uses Drupal CMS (we plan to continue using Drupal CMS) and at the moment, a toy front-end is based on the Drupal Skeleton platform for its simplicity, clean UI and mobile device friendliness. The web developer / designer can choose any Drupal front end as a starting point or come up with a new Drupal template that meets our requirements below. Prior experience and expertise on Drupal would be great.

2. Audience profile: While the primary audience for the website is expected to be young kids (6-10 years) not very familiar with English, the secondary audience also includes adults interested in basic English language skills. So the overall goal is to have simple, uncluttered / clean, elegant and lightweight (think loading time as well as mobile device friendliness) interface that is extremely intuitive and easy to navigate, is artistic and aesthetically appealing to a wide audience (especially the non-native English speaking populations). The most important point is that our target audience should feel welcome with the clean, crisp look and easy, user-centric navigation, and should in no case feel overwhelmed (say with too much text or clutter on the front page).

3. Front page: Here is a currently envisioned preliminary sketch of the website front page (very much open for refinement and improvements)
a. The top “menu bar” part of the landing page will have our organization name and logo along with (or above) the top menu bar with the following links and sub-links
i. “Learn” link with sub-menu of all our content sections (World learning, Basic sentence learning, Classic short stories, Picture Dictionary)
ii. “About” links with information about us (sub-menu entries: About PAVO Tides, Team, Supporters, Contributors)
iii. “Contribute” link with sub-menu entries Donate, Volunteer
iv. Menu entries towards the right side: “Login / sign up” followed by
v. “Search” with space to enter the search phrase
b. The middle “main page content” part of the page is where we would have entry points to our main content categories. The portion is envisioned to be graphical, with big blocks (images) as links to our content categories. The current categories (to start with) include 1. Word learning, 2. Basic sentence learning, and 3. Classic stories. We welcome creative ideas to represent these content categories in an appealing and elegant way (for example, these content categories could be portrayed as closed double doors that lead to the pages with the content. We would like to have placeholders for appropriate image links to different content categories – we should be able to put appropriate images or change them as we come up with new ideas that would work best with our target audience). The categories would change and grow as our content evolves, hence the core idea is to build a flexible framework that readily allows for expansion as well as customization.
c. The bottom menu / links bar portion of the landing page will have a list of links that are not included at the top. Examples include (with flexibility needed to add more when needed)
i. “Help”: this leads to a new page with FAQ, How to use
ii. “Contact us” link to a web contact form page
iii. “For Teachers” link to a page with information such as how to use, tips, pilot programs,
iv. “Volunteer” link to page with links such as Donate, Volunteer
v. “Contributors” that would link to a page with information about our Artists, Teachers, Writers, Developers etc.
vi. “Jobs” would link to a jobs page
vii. “Blog” would lead to our blog page
viii. “User stories” link to pages with feedback that we obtain from the users about how the content has helped them,
ix. Web 2.0 placeholders for social media (to be added later)

d. The footer of the website should include text “2013 PAVO Tides, All rights reserved.”

4. The middle block of the front page is the largest in screen real estate and perhaps the most challenging part that requires much creativity and thought on the UI/UX design aspect – the content pages pointed to by the section links on the middle portion of the front page are also being designed.

5. Color preference is towards soft, elegant (think grays, whites, light blues, other light colors) web safe colors. No harsh (too bright, garish) colors.

6. Fonts preference Nice, clean looking fonts (Arial alright) compatible across browsers.

7. Portability and robustness of the front page layout for different platforms should be carefully considered. Although our first launch target platform is PC (where cross browser compatibility is important), this would very soon be followed by mobile devices such as tablets and smartphones given their prevalence across the globe. This mobile friendly design or easy portability to mobile platforms with little work requirement should be considered as a design requirement.

8. Front page as a framework for the complete website: Note that the top and the bottom portions of the front page are envisioned be used as a common template / frame across all the pages of our website – the middle portion would be used to show our content on the other pages of our website.

9. UX: For the UI/UX design, it is critical to keep in mind key qualities such as ease of use, simplicity, elegance and artistic appeal. Some specific points to keep in mind: (1) the major portion of the target audience would be new to English and (2) young children are expected to be the primary audience but we want the website to appeal to adults interested in learning as well, and (3) we need the website to work even with relatively slow Internet speeds (for underdeveloped / developing regions especially), should always be kept in mind. HTML5 compliance ideas are encouraged.

10. Strictly not desired: Typical corporate feel seen in many webpages, blocky graphics, dull and uninviting overall look with no personality, Flash type effects, harsh colors.

11. Creativity and imagination necessary: We would like to reiterate that the designer/developer has complete freedom to re-imagine the front page considering the above requirements and get back with ideas for an inspiring layout that presents the content outlined above in an intuitive format, carefully considering our target audience.

A note: As a rule, we will always make sure that our developers and artists get proper credit for their work and are recognized and acknowledged by everyone visiting our website.

Expected deliverables:
Website design psd files AND coded webpage / Drupal template: the corresponding source code and all the required libraries, images etc would be required with minimal documentation / pointers on how to make changes and customizations.

Interested developers are encouraged to first send us preliminary prototype Design for the front page to get feedback on whether their approach and style is in line with our needs and preferences. We will suggest the developers to proceed further if the team thinks there is some potential for a match (of course, the final determination would be from the pool of shortlisted submissions) – otherwise, in case the team does not see potential for a match with our needs or if we have already received multiple submissions that are comparatively more closely aligned with our vision for the website, we'd prefer to be respectful of the developers’ time and effort by requesting them not to proceed further.

Please consider this effort as your contribution to an important social cause of global and accessible online education and not a commercial enterprise (our passion for making a positive impact is what is driving the PAVO Tides nonprofit team to undertake this initiative!). We would like to invite you to join us in this effort!

Reason: Due to requests from interested designers, we are extending the deadline. Looking forward to receiving many other creative designs!

Please see the project brief.

• Please see the project brief.

```html
<!DOCTYPE html>
<html lang="en">
<head>
<meta charset="utf-8">
<title>PAVO Tides</title>
<link rel="stylesheet" href="https://fonts.googleapis.com/css2?family=Ubuntu:wght@400;500;700&family=Shadows+Into+Light&display=swap">
<style>
  :root {
    --ink: #111111;
    --nav-blue: #b6dcfb;
    --card-pink: #fdb6ec;
    --card-violet: #b6c0fe;
    --card-peach: #fdd6b5;
    --footer-grey: #e2e2e2;
    --footer-text: #7b7b7b;
    --bar-black: #000000;
    --bar-text: #9a9a9a;
    --page: #ffffff;
  }
  * { box-sizing: border-box; margin: 0; padding: 0; }
  html, body { width: 1088px; height: 1200px; overflow: hidden; background: var(--page); }
  body { position: relative; font-family: "Ubuntu", Arial, sans-serif; color: var(--ink); }
  a { color: inherit; text-decoration: none; }
  .abs { position: absolute; }

  .brand { left: 42px; top: 22px; font-size: 36px; font-weight: 500; color: var(--ink); }
  .account { top: 36px; font-size: 17px; color: #444; }
  .account.login { left: 845px; }
  .account.signup { left: 935px; }

  .nav-band { left: 201px; top: 132px; width: 842px; height: 94px; background: linear-gradient(#e2e2e2, #ececec); }
  .nav-active { left: 42px; top: 111px; width: 159px; height: 115px; background: var(--nav-blue); }
  .nav-link { top: 152px; font-family: "Shadows Into Light", cursive; font-size: 32px; color: #333; transform: translateX(-50%); white-space: nowrap; }
  .search-field { left: 593px; top: 160px; width: 313px; height: 31px; background: #fff; border: 1px solid #c9c9c9; }
  .search-label { left: 936px; top: 164px; font-size: 18px; color: #555; }

  .sub-nav { left: 42px; top: 226px; width: 1001px; height: 54px; background: var(--nav-blue);
    display: flex; justify-content: center; align-items: center; gap: 26px; font-size: 14.5px; color: #111; }

  .credit { right: 45px; top: 301px; font-size: 9px; color: #aaa; }

  .letter-art { top: 352px; height: 226px; border-radius: 6px; }
  .art-a { left: 77px;  width: 186px; background: radial-gradient(circle at 60% 55%, #e2473a 0, #f29a8c 45%, #fbe7e4 75%, #ffffff 100%); }
  .art-b { left: 328px; width: 213px; background: radial-gradient(circle at 58% 58%, #2f9ee3 0, #8fccf2 45%, #eaf5fd 75%, #ffffff 100%); }
  .art-c { left: 589px; width: 170px; background: radial-gradient(circle at 50% 60%, #f6b021 0, #f9d47a 45%, #fdf3dc 75%, #ffffff 100%); }
  .art-d { left: 823px; width: 212px; background: radial-gradient(circle at 62% 58%, #2fb39a 0, #8fd9c8 45%, #e6f7f3 75%, #ffffff 100%); }

  .category { top: 678px; width: 298px; }
  .category .tile { height: 88px; display: flex; align-items: center; justify-content: center;
    font-family: "Shadows Into Light", cursive; font-size: 32px; color: #111; white-space: nowrap; }
  .category p { margin-top: 16px; font-size: 12.3px; font-weight: 500; line-height: 25.5px; text-align: justify; text-align-last: left; }
  .category .more { position: absolute; right: 0; bottom: -6px; font-size: 16px; font-weight: 500; letter-spacing: -1px; }
  .cat-word { left: 42px; } .cat-word .tile { background: var(--card-pink); }
  .cat-sentence { left: 393px; } .cat-sentence .tile { background: var(--card-violet); }
  .cat-stories { left: 745px; } .cat-stories .tile { background: var(--card-peach); }

  .footer-links { left: 42px; top: 992px; width: 1001px; height: 157px; background: var(--footer-grey); }
  .link-col { position: absolute; top: 26px; list-style: none; font-size: 15px; color: var(--footer-text); line-height: 25.5px; }
  .col-help { left: 107px; } .col-community { left: 457px; } .col-social { left: 819px; }
  .current-mark { position: absolute; left: 80px; top: 26px; font-size: 14px; font-weight: 500; letter-spacing: -1px; line-height: 25.5px; color: var(--ink); }

  .footer-bar { left: 42px; top: 1149px; width: 1001px; height: 46px; background: var(--bar-black);
    font-size: 12.5px; color: var(--bar-text); }
  .footer-bar .copyright { position: absolute; left: 106px; top: 14px; }
  .footer-bar .legal { position: absolute; left: 745px; top: 14px; }
  .footer-bar .legal span { margin: 0 12px; }
</style>
</head>
<body>
  <header>
    <a class="abs brand" href="#">PAVO Tides</a>
    <a class="abs account login" href="#">LOGIN</a>
    <a class="abs account signup" href="#">SIGN UP</a>

    <nav aria-label="Main">
      <div class="abs nav-band"></div>
      <div class="abs nav-active"></div>
      <a class="abs nav-link" style="left:122px" href="#">Learn</a>
      <a class="abs nav-link" style="left:294px" href="#">About</a>
      <a class="abs nav-link" style="left:463px" href="#">Contribute</a>
      <div class="abs search-field" role="search"></div>
      <span class="abs search-label">SEARCH</span>
    </nav>

    <nav class="abs sub-nav" aria-label="Learn">
      <a href="#">WORLD LEARNING</a><span>|</span>
      <a href="#">BASIC SENTENCE LEARNING</a><span>|</span>
      <a href="#">CLASSIC SHORT STORIES</a><span>|</span>
      <a href="#">PICTURE DICTIONARY</a>
    </nav>
  </header>

  <main>
    <p class="abs credit">http://www.artpantry.com/free-art/cheerful-alphabet-letters-with-children-set-a-to-d</p>

    <div class="abs letter-art art-a" role="img" aria-label="Cartoon child holding a gift beside a red crayon letter A"></div>
    <div class="abs letter-art art-b" role="img" aria-label="Cartoon child with a heart balloon beside a blue crayon letter B"></div>
    <div class="abs letter-art art-c" role="img" aria-label="Cartoon child sitting on a yellow crayon letter C"></div>
    <div class="abs letter-art art-d" role="img" aria-label="Cartoon child with a lollipop beside a green crayon letter D"></div>

    <section class="abs category cat-word">
      <div class="tile">Word learning</div>
      <p>Lorem ipsum dolor sit amet, consectetur adipiscing elit. Aenean vulputate vitae quam eu venenatis. In eu lacus nisi. Aenean nec tortor a neque pretium adipiscing quis nec quam. Quisque commodo tortor quis pharetra adipiscing. In non blandit risus. Quisque vel justo ipsum. Donec blandit lacus id urna semper, quis posuere ante pulvinar.</p>
      <a class="more" href="#">&gt;&gt;</a>
    </section>
    <section class="abs category cat-sentence">
      <div class="tile">Basic sentence learning</div>
      <p>Lorem ipsum dolor sit amet, consectetur adipiscing elit. Aenean vulputate vitae quam eu venenatis. In eu lacus nisi. Aenean nec tortor a neque pretium adipiscing quis nec quam. Quisque commodo tortor quis pharetra adipiscing. In non blandit risus. Quisque vel justo ipsum. Donec blandit lacus id urna semper, quis posuere ante pulvinar.</p>
      <a class="more" href="#">&gt;&gt;</a>
    </section>
    <section class="abs category cat-stories">
      <div class="tile">Classic stories.</div>
      <p>Lorem ipsum dolor sit amet, consectetur adipiscing elit. Aenean vulputate vitae quam eu venenatis. In eu lacus nisi. Aenean nec tortor a neque pretium adipiscing quis nec quam. Quisque commodo tortor quis pharetra adipiscing. In non blandit risus. Quisque vel justo ipsum. Donec blandit lacus id urna semper, quis posuere ante pulvinar.</p>
      <a class="more" href="#">&gt;&gt;</a>
    </section>
  </main>

  <footer>
    <div class="abs footer-links">
      <span class="current-mark">&gt;&gt;</span>
      <ul class="link-col col-help">
        <li><a href="#">Help</a></li>
        <li><a href="#">Contact us</a></li>
        <li><a href="#">For Teachers</a></li>
        <li><a href="#">Volunteer</a></li>
      </ul>
      <ul class="link-col col-community">
        <li><a href="#">Contributors</a></li>
        <li><a href="#">Jobs</a></li>
        <li><a href="#">Blog</a></li>
        <li><a href="#">User stories</a></li>
      </ul>
      <ul class="link-col col-social">
        <li><a href="#">Circlepage</a></li>
        <li><a href="#">Chirpline</a></li>
        <li><a href="#">Roomspace</a></li>
        <li><a href="#">Workweave</a></li>
      </ul>
    </div>
    <div class="abs footer-bar">
      <span class="copyright">2013 PAVO Tides, All rights reserved</span>
      <span class="legal"><a href="#">T&amp;S</a><span>|</span><a href="#">Privicy Policies</a></span>
    </div>
  </footer>
</body>
</html>
```